Dog grooming business card
This is a business card for m dog grooming business like it say above.
In the priorities box below I will have the text that I want on the card.

Industry/Entity Type

Business

Colors

Designer to choose colors to be used in the design.

Requirements
Must have
• My logo and the insurance stamp must be on the card.

Text it must have :

Professional grooming services
Email: lunabrisk@mailvane.net
Text or call 1 705 318 6642
TKV certified/member
Pet first aid certified
Next appointment ___________________________________
Nice to have
• Greens to match my logo

```html
<!DOCTYPE html>
<html lang="en">
<head>
<meta charset="utf-8">
<title>Luna Brisk – Grooming Business Card</title>
<link rel="stylesheet" href="https://fonts.googleapis.com/css2?family=Lobster&family=Arimo:wght@400;700&display=swap">
<style>
  :root {
    --bg: #d9dce0;
    --card-white: #ffffff;
    --card-front: #f6faf9;
    --ink: #1d1b1c;
    --green: #8cc63f;
    --green-text: #9bcf3f;
    --dark: #1a1718;
    --light-text: #f2f2f2;
    --dots: #2a2a2a;
  }
  * { box-sizing: border-box; margin: 0; padding: 0; }
  html, body { width: 1200px; height: 960px; overflow: hidden; }
  body {
    background: var(--bg);
    font-family: "Arimo", Arial, sans-serif;
    position: relative;
  }
  .card {
    position: absolute;
    left: 290px;
    width: 620px;
    height: 354px;
    border-radius: 18px;
    overflow: hidden;
    box-shadow: 0 10px 30px rgba(0,0,0,0.18);
  }
  .card-front { top: 72px; background: var(--card-front); }
  .card-back { top: 520px; background: var(--card-white); }

  .brand {
    display: flex;
    align-items: center;
    justify-content: center;
    gap: 12px;
  }
  .brand-dot {
    width: 22px; height: 22px;
    border-radius: 50%;
    background: var(--green);
  }
  .brand-name {
    font-family: "Lobster", cursive;
    font-size: 44px;
    color: var(--ink);
  }

  .card-front .brand { margin-top: 78px; }
  .next-appointment {
    text-align: center;
    margin-top: 28px;
    color: var(--green-text);
    font-size: 17px;
  }
  .write-line {
    margin: 12px auto 0;
    width: 470px;
    border-top: 3px dotted var(--dots);
  }
  .contact {
    margin: 22px auto 0;
    text-align: center;
    font-size: 17px;
    color: var(--ink);
  }
  .contact .label { color: var(--green-text); }

  .back-top {
    height: 196px;
    display: flex;
    flex-direction: column;
    align-items: center;
    justify-content: flex-end;
    padding-bottom: 12px;
  }
  .back-top .brand { margin-bottom: 8px; }
  .back-top .brand-name { font-size: 36px; }
  .tagline {
    font-family: "Lobster", cursive;
    font-size: 38px;
    color: var(--ink);
  }
  .stripe { height: 10px; background: var(--green); }
  .back-bottom {
    height: 148px;
    background: var(--dark);
    color: var(--light-text);
    text-align: center;
    padding-top: 24px;
    font-size: 17px;
    line-height: 1.45;
  }
  .badge {
    display: block;
    margin: 12px auto 0;
  }
</style>
</head>
<body>

<section class="card card-front" aria-label="Card front">
  <div class="brand">
    <span class="brand-dot"></span>
    <span class="brand-name">Luna Brisk</span>
  </div>
  <p class="next-appointment">Next appointment</p>
  <div class="write-line"></div>
  <p class="contact">
    <span class="label">Email</span> lunabrisk@mailvane.net /
    <span class="label">Text</span> or <span class="label">call</span> 1 705 318 6642
  </p>
</section>

<section class="card card-back" aria-label="Card back">
  <div class="back-top">
    <div class="brand">
      <span class="brand-dot"></span>
      <span class="brand-name">Luna Brisk</span>
    </div>
    <h1 class="tagline">Professional grooming services</h1>
  </div>
  <div class="stripe"></div>
  <div class="back-bottom">
    <p>TKV certified/member</p>
    <p>Pet first aid certified</p>
    <svg class="badge" width="96" height="38" viewBox="0 0 96 38" role="img" aria-label="Insurance stamp">
      <rect x="1" y="1" width="94" height="36" rx="6" fill="#ffffff" stroke="#2a6fc4" stroke-width="2"/>
    </svg>
  </div>
</section>

</body>
</html>
```